" A clínica já existe há 15 anos, atendendo a classe "C". Já possui uma logo há 8 anos. Este serviço solicitado será para uma nova sede que atenderá o público "A". O produto principal desta nova clínica é o aparelho estético (invisível). "

```html
<!DOCTYPE html>
<html lang="pt-BR">
<head>
<meta charset="utf-8">
<title>Cartão de Visitas – Ricardo Valente Ortodontia Invisível</title>
<link href="https://fonts.googleapis.com/css2?family=Montserrat:wght@400;500;600&display=swap" rel="stylesheet">
<style>
  :root{
    --bg:#dcdcdc;
    --ink:#1b1b1b;
    --card-dark:#0e0e0e;
    --card-dark-2:#262626;
    --card-light:#ffffff;
    --silver:#b9b9b9;
    --silver-light:#e6e6e6;
    --muted:#8a8a8a;
  }
  *{box-sizing:border-box;margin:0;padding:0}
  html,body{width:1200px;height:1200px;overflow:hidden}
  body{
    background:radial-gradient(circle at 50% 45%, #f1f1f1 0%, var(--bg) 75%);
    font-family:"Montserrat", sans-serif;
    color:var(--ink);
    position:relative;
  }
  .sheet-title{
    position:absolute;top:44px;left:48px;
    font-size:20px;font-weight:500;letter-spacing:.5px;
  }
  .card{
    position:absolute;left:220px;width:760px;height:420px;
    box-shadow:0 18px 40px rgba(0,0,0,.25);
    overflow:hidden;
  }
  /* back side */
  .card--back{
    top:130px;
    background:linear-gradient(135deg, var(--card-dark-2) 0%, var(--card-dark) 45%, #050505 100%);
    color:var(--silver-light);
  }
  .card--back .sheen{
    position:absolute;left:-80px;top:-60px;width:420px;height:420px;border-radius:50%;
    background:radial-gradient(circle, rgba(255,255,255,.08) 0%, rgba(255,255,255,0) 70%);
  }
  .brand-small{
    position:absolute;left:60px;top:110px;width:260px;text-align:center;
  }
  .brand-mark{
    display:block;margin:0 auto 18px;border-radius:50%;
    background:var(--silver);
  }
  .brand-small .brand-mark{width:64px;height:64px}
  .brand-name{font-weight:500;text-transform:uppercase;letter-spacing:1px}
  .brand-small .brand-name{font-size:24px;color:var(--silver-light)}
  .brand-tag{
    display:flex;align-items:center;gap:8px;justify-content:center;
    text-transform:uppercase;letter-spacing:2.5px;
  }
  .brand-tag::before,.brand-tag::after{content:"";flex:1;height:1px;background:currentColor}
  .brand-small .brand-tag{font-size:9px;color:var(--muted);margin-top:6px}
  .divider{position:absolute;left:350px;top:70px;width:1px;height:210px;background:#5a5a5a}
  .contacts{
    position:absolute;right:46px;top:78px;list-style:none;text-align:right;
    font-size:13px;line-height:1.5;color:var(--silver-light);
  }
  .contacts li{display:flex;align-items:center;justify-content:flex-end;gap:12px;margin-bottom:18px}
  .contacts .icon{width:22px;height:22px;flex:none}
  .website{
    position:absolute;left:0;right:0;bottom:58px;text-align:center;
    font-size:17px;letter-spacing:6px;color:var(--silver-light);
  }
  /* front side */
  .card--front{top:620px;background:var(--card-light)}
  .brand-large{position:absolute;left:0;right:0;top:70px;text-align:center}
  .brand-large .brand-mark{width:110px;height:110px;background:var(--ink)}
  .brand-large .brand-name{font-size:44px;color:var(--ink);letter-spacing:1.5px}
  .brand-large .brand-tag{
    font-size:13px;color:#555;width:430px;margin:6px auto 0;letter-spacing:3px;
  }
  .front-band{
    position:absolute;left:0;right:0;bottom:0;height:60px;
    background:linear-gradient(180deg,#2a2a2a,#000);
  }
  .front-band::before{
    content:"";position:absolute;left:0;right:0;top:-8px;height:8px;
    background:linear-gradient(90deg,var(--silver-light),#9a9a9a,var(--silver-light));
  }
</style>
</head>
<body>
  <h1 class="sheet-title">CARTÃO DE VISITAS</h1>

  <section class="card card--back" aria-label="Verso do cartão">
    <div class="sheen"></div>
    <div class="brand-small">
      <span class="brand-mark"></span>
      <p class="brand-name">Ricardo Valente</p>
      <p class="brand-tag">Ortodontia Invisível</p>
    </div>
    <div class="divider"></div>
    <ul class="contacts">
      <li>(51) 3210-4580
        <svg class="icon" viewBox="0 0 22 22"><circle cx="11" cy="11" r="11" fill="#9a9a9a"/><path d="M7 6.5c.5-.5 1.3-.5 1.7 0l1 1.3c.3.4.3 1-.1 1.3l-.6.5c.6 1.3 1.6 2.3 2.9 2.9l.5-.6c.4-.4.9-.4 1.3-.1l1.3 1c.5.4.5 1.2 0 1.7l-.7.7c-3.5.5-8-4-7.5-7.5z" fill="#111"/></svg>
      </li>
      <li>(51) 99801-2245 / 98762-1030
        <svg class="icon" viewBox="0 0 22 22"><circle cx="11" cy="11" r="11" fill="#9a9a9a"/><rect x="8" y="5" width="6" height="12" rx="1.2" fill="#111"/></svg>
      </li>
      <li>Rua das Acácias, 120/704<br>Jardim Alto – Porto Sereno RS
        <svg class="icon" viewBox="0 0 22 22"><circle cx="11" cy="11" r="11" fill="#9a9a9a"/><path d="M11 5a4 4 0 0 0-4 4c0 3 4 8 4 8s4-5 4-8a4 4 0 0 0-4-4zm0 5.5a1.5 1.5 0 1 1 0-3 1.5 1.5 0 0 1 0 3z" fill="#111"/></svg>
      </li>
    </ul>
    <p class="website">www.ricardovalente.com.br</p>
  </section>

  <section class="card card--front" aria-label="Frente do cartão">
    <div class="brand-large">
      <span class="brand-mark"></span>
      <p class="brand-name">Ricardo Valente</p>
      <p class="brand-tag">Ortodontia Invisível</p>
    </div>
    <div class="front-band"></div>
  </section>
</body>
</html>
```